** Wanted ** Wordpress web design for scaffolding rental and construction company

We need a website design and must be functional to show a basic overview of what our company offers as a service. We have a domain name and a logo but we need web design. This web site should have another scaffolding rental page for construction and renovation as well as a quote section where customers can enter their personal information and also upload photos. The site% 26quot; www.corvithane.com% 26quot; should be intuitive, clear and classy ... The logo must be found on the site in several ways.

Target Market(s)

Professional and no professional

Coding

Coded - Design and coding required

Number of Pages Required

3 page

Font styles to use
Serif
Sans Serif
Decorative
Script

Requirements
Must have
• Our logo
Nice to have
• Slogan:% 26quot; The height% 26 # 224; port% 26 # 233; e hand% 26quot;

```html
<!DOCTYPE html>
<html lang="en">
<head>
<meta charset="utf-8">
<title>Corvithane — Scaffolding Rental &amp; Construction</title>
<link href="https://fonts.googleapis.com/css2?family=Montserrat:wght@400;500;600;700;800;900&family=Orbitron:wght@500;600&family=Open+Sans:wght@400;600&display=swap" rel="stylesheet">
<style>
:root{
  --orange:#f0821e;
  --orange-dark:#d96e0f;
  --ink:#1b1b1b;
  --dark:#232323;
  --panel:#2a2a2a;
  --blue:#1a90d9;
  --blue-deep:#0f6fb3;
  --page:#f3f3f3;
  --grey:#8a8a8a;
  --ghost:#e2e2e2;
  --white:#ffffff;
}
*{margin:0;padding:0;box-sizing:border-box}
html,body{width:1200px;height:5204px;overflow:hidden}
body{background:var(--page);font-family:"Montserrat",sans-serif;color:var(--ink);position:relative}
.abs{position:absolute}
.caps{text-transform:uppercase;letter-spacing:2px}

/* top bar + nav */
.topbar{left:0;top:0;width:1200px;height:36px;background:#141414;z-index:3}
.topbar .info{position:absolute;top:12px;font-size:9px;color:#bdbdbd;font-family:"Open Sans",sans-serif;display:flex;align-items:center;gap:7px}
.topbar .info i{width:12px;height:12px;background:var(--orange);transform:rotate(45deg);display:inline-block}
.nav{left:0;top:36px;width:1200px;height:62px;z-index:3;border-bottom:1px solid rgba(255,255,255,.12)}
.nav a{position:absolute;top:25px;font-size:10px;font-weight:700;color:#fff;text-decoration:none;letter-spacing:1px;text-transform:uppercase;transform:translateX(-50%)}
.nav a.active{color:var(--orange)}
.brand{display:flex;align-items:center;gap:8px;font-weight:800;font-size:13px;letter-spacing:2px;color:#fff;text-transform:uppercase}
.brand i{width:12px;height:12px;background:var(--orange);display:inline-block}
.nav .brand{position:absolute;left:600px;top:22px;transform:translateX(-50%)}

/* hero */
.hero{left:0;top:0;width:1200px;height:748px}
.hero-ghost{left:0;top:200px;width:1200px;text-align:center;font-size:96px;font-weight:900;color:rgba(255,255,255,.08);letter-spacing:6px;z-index:1}
.hero-title{left:0;top:196px;width:1200px;text-align:center;font-size:50px;line-height:62px;font-weight:900;color:#fff;letter-spacing:3px;z-index:2}
.hero-title span{color:var(--orange)}
.hero-sub{left:271px;top:337px;width:666px;height:33px;background:#fff;font-size:11px;letter-spacing:2px;text-align:center;line-height:33px;color:#333;z-index:2}
.btn{position:absolute;height:44px;line-height:44px;text-align:center;font-size:10px;font-weight:700;letter-spacing:2px;text-transform:uppercase;color:#fff}
.btn-orange{background:var(--orange)}
.btn-dark{background:var(--ink);border:3px solid var(--orange);line-height:38px}
.scroll{left:0;top:632px;width:1200px;text-align:center;font-size:8px;color:#ddd;letter-spacing:2px;z-index:2}

/* section headings */
.ghost{position:absolute;font-weight:900;color:var(--ghost);letter-spacing:4px;white-space:nowrap}
.heading{position:absolute;font-weight:900;font-size:36px;letter-spacing:3px;text-transform:uppercase;white-space:nowrap}

/* service cards */
.card{position:absolute;width:268px;height:174px;background:#fff;border-bottom:4px solid var(--orange);box-shadow:0 4px 14px rgba(0,0,0,.08);text-align:center}
.card.featured{background:var(--orange)}
.card .num{margin-top:70px;font-size:10px;letter-spacing:2px;color:var(--grey);text-transform:uppercase}
.card .name{margin-top:8px;font-size:14px;font-weight:800;letter-spacing:1px;line-height:16px;text-transform:uppercase}
.card .more{margin-top:14px;font-size:10px;letter-spacing:2px;color:var(--orange);font-weight:600;text-transform:uppercase}
.card.featured .num,.card.featured .name,.card.featured .more{color:#fff}
.card .icon{position:absolute;left:50%;top:-40px;margin-left:-40px;width:80px;height:80px}

/* why us */
.stat{position:absolute;width:194px;height:169px;border:4px solid var(--orange);background:rgba(20,20,20,.6);text-align:center;color:#fff}
.stat b{display:block;margin-top:36px;font-family:"Orbitron",sans-serif;font-weight:600;font-size:50px;color:var(--orange);letter-spacing:4px}
.stat span{display:block;margin-top:10px;font-size:10px;letter-spacing:2px;line-height:17px;text-transform:uppercase}
.why-text{left:300px;top:1917px;width:600px;text-align:center;font-family:"Open Sans",sans-serif;font-size:11px;line-height:20px;color:#fff}
.cta{left:174px;top:2030px;width:854px;height:162px;background:var(--blue);box-shadow:0 8px 18px rgba(0,0,0,.2)}
.cta p{position:absolute;left:64px;top:70px;font-size:16px;font-weight:700;letter-spacing:3px;color:#14233a}

/* about */
.about-box{left:630px;top:2400px;width:392px;height:242px;background:#fff;box-shadow:0 2px 10px rgba(0,0,0,.06);padding:26px 28px;font-family:"Open Sans",sans-serif;font-size:10.5px;line-height:19px;color:#777}
.about-box p+p{margin-top:18px}

/* quote */
.quote{left:162px;top:2848px;width:876px;height:394px;background:linear-gradient(135deg,#262626,#1c1c1c 60%,#2a2a2a)}
.field{position:absolute;background:#fff;font-family:"Open Sans",sans-serif;font-size:10px;color:#777;text-align:center}
.upload{position:absolute;left:56px;top:255px;width:764px;height:99px;border:2px dashed #6a6a6a;color:#fff;text-align:center;font-family:"Open Sans",sans-serif;font-size:10px}

/* portfolio */
.portfolio{left:0;top:3377px;width:1200px;height:713px;background:linear-gradient(180deg,#1e95dc,#1782c9);border-top:14px solid var(--orange);border-bottom:14px solid var(--orange)}
.shot{position:absolute;top:3571px;height:317px}
.shot-a{background:linear-gradient(180deg,#5aa7e0 0%,#9ec6e6 30%,#b0773e 60%,#6b4a2c 100%)}
.shot-b{background:linear-gradient(180deg,#4c9de0 0%,#a9d0ef 35%,#3d8b4a 58%,#7a5a3a 100%)}
.feature{left:460px;top:3563px;width:283px;height:333px;background:linear-gradient(180deg,#303030,#1f1f1f);}
.feature .frame{position:absolute;left:36px;top:36px;width:211px;height:261px;border:3px solid var(--orange);text-align:center;color:#fff}
.arrow-btn{position:absolute;top:3706px;width:48px;height:48px;background:var(--ink);color:#fff;font-size:20px;line-height:48px;text-align:center}

/* news */
.news{position:absolute;top:4278px;width:268px;height:328px;background:#fff;box-shadow:0 2px 10px rgba(0,0,0,.06)}
.news .img{height:146px}
.news .body{padding:14px 16px}
.news .date{font-size:10px;letter-spacing:2px;color:#999}
.news h3{margin-top:8px;font-size:13px;font-weight:800;letter-spacing:1px}
.news p{margin-top:10px;font-family:"Open Sans",sans-serif;font-size:9.5px;line-height:17px;color:#888}
.news .more{margin-top:12px;font-size:10px;letter-spacing:2px;color:var(--orange);font-weight:600}

/* footer */
.footer{left:0;top:4723px;width:1200px;height:481px;background:linear-gradient(180deg,#242424,#1a1a1a)}
.fcol{position:absolute;top:115px}
.fcol h4{font-size:11px;font-weight:800;letter-spacing:2px;color:#fff;margin-bottom:24px}
.fcol li{list-style:none;font-size:9.5px;letter-spacing:2px;color:#a0a0a0;height:36px;text-transform:uppercase}
.fcol li.hl{color:var(--orange)}
.fcol li i{display:inline-block;width:8px;height:8px;border-radius:50%;background:#777;margin-right:8px}
.copy{position:absolute;left:174px;top:436px;font-size:9px;color:#888;font-family:"Open Sans",sans-serif}
.social{position:absolute;top:432px;width:14px;height:14px;border-radius:50%;background:#6a6a6a}
</style>
</head>
<body>

<!-- HERO -->
<svg class="abs hero" width="1200" height="748" viewBox="0 0 1200 748" role="img" aria-label="Building under construction wrapped in scaffolding, silhouetted against a dusk sky">
  <defs>
    <linearGradient id="sky" x1="0" y1="0" x2="0" y2="1">
      <stop offset="0" stop-color="#1b2c47"/>
      <stop offset=".35" stop-color="#3e5f86"/>
      <stop offset=".62" stop-color="#b7773d"/>
      <stop offset=".8" stop-color="#e59a3a"/>
      <stop offset="1" stop-color="#2b1d12"/>
    </linearGradient>
  </defs>
  <polygon points="0,0 1200,0 1200,606 600,748 0,606" fill="url(#sky)"/>
  <polygon points="0,570 600,700 1200,570 1200,606 600,748 0,606" fill="#f0821e"/>
  <polygon points="480,720 600,748 720,720 600,690" fill="#1c1c1c"/>
</svg>

<div class="abs topbar">
  <div class="info" style="left:170px"><i></i>(555) 010 2040</div>
  <div class="info" style="left:326px"><i></i>Address Line 1, City, State, Zip Code</div>
  <div class="info" style="left:676px"><i></i>info@corvithane.com</div>
  <div class="info" style="left:826px"><i></i>Mon - Fri : 9am to 8pm, Sun : Holiday</div>
</div>

<nav class="abs nav">
  <a class="active" style="left:230px">Home</a>
  <a style="left:343px">About Us</a>
  <a style="left:456px">Services</a>
  <div class="brand"><i></i>Corvithane</div>
  <a style="left:743px">News</a>
  <a style="left:856px">Contact</a>
  <a style="left:969px">Get a Quote</a>
</nav>

<div class="abs hero-ghost">CORVITHANE</div>
<h1 class="abs hero-title">LET'S <span>ELEVATE</span> YOUR<br>DREAM BUILDING</h1>
<div class="abs hero-sub">A CATCHY SUBTITLE OR CAPTION GOES HERE. LOREM IPSUM DOLOR SIT AMET CONSECTETUR.</div>
<div class="btn btn-orange" style="left:440px;top:422px;width:148px;z-index:2">Our Services</div>
<div class="btn btn-dark" style="left:614px;top:422px;width:148px;z-index:2">Get a Quote</div>
<div class="abs scroll">SCROLL FOR MORE</div>
<svg class="abs" style="left:592px;top:656px;z-index:2" width="16" height="22" viewBox="0 0 16 22"><rect x="1" y="1" width="14" height="20" rx="7" fill="none" stroke="#fff" stroke-width="1.5"/><line x1="8" y1="5" x2="8" y2="9" stroke="#fff" stroke-width="1.5"/></svg>

<!-- SERVICES -->
<div class="ghost" style="left:0;width:1200px;text-align:center;top:822px;font-size:76px">SERVICES</div>
<h2 class="heading" style="left:0;width:1200px;text-align:center;top:852px">Services</h2>

<div class="card" style="left:174px;top:970px">
  <svg class="icon" viewBox="0 0 80 80"><rect x="16" y="16" width="48" height="48" transform="rotate(45 40 40)" fill="var(--orange)"/><g stroke="#fff" stroke-width="2" fill="none"><rect x="30" y="24" width="20" height="32"/><line x1="30" y1="35" x2="50" y2="35"/><line x1="30" y1="46" x2="50" y2="46"/><line x1="40" y1="24" x2="40" y2="56"/></g></svg>
  <div class="num">Service 1</div><div class="name">Commercial<br>Scaffolding</div><div class="more">Learn More</div>
</div>
<div class="card featured" style="left:465px;top:970px">
  <svg class="icon" viewBox="0 0 80 80"><rect x="16" y="16" width="48" height="48" transform="rotate(45 40 40)" fill="#fff"/><g stroke="#333" stroke-width="2" fill="none"><rect x="30" y="30" width="20" height="26"/><polyline points="28,31 40,22 52,31"/><line x1="30" y1="43" x2="50" y2="43"/><line x1="40" y1="30" x2="40" y2="56"/></g></svg>
  <div class="num">Service 2</div><div class="name">Domestic<br>Scaffolding</div><div class="more">Learn More</div>
</div>
<div class="card" style="left:757px;top:970px">
  <svg class="icon" viewBox="0 0 80 80"><rect x="16" y="16" width="48" height="48" transform="rotate(45 40 40)" fill="var(--orange)"/><g stroke="#fff" stroke-width="2" fill="none"><rect x="28" y="32" width="24" height="24"/><polyline points="28,32 34,24 46,24 52,32"/><line x1="28" y1="44" x2="52" y2="44"/><line x1="40" y1="32" x2="40" y2="56"/></g></svg>
  <div class="num">Service 3</div><div class="name">Industrial<br>Scaffolding</div><div class="more">Learn More</div>
</div>
<div class="card" style="left:174px;top:1210px">
  <svg class="icon" viewBox="0 0 80 80"><rect x="16" y="16" width="48" height="48" transform="rotate(45 40 40)" fill="var(--orange)"/><g stroke="#fff" stroke-width="2" fill="none"><line x1="32" y1="22" x2="32" y2="58"/><line x1="48" y1="22" x2="48" y2="58"/><line x1="32" y1="30" x2="48" y2="44"/><line x1="48" y1="30" x2="32" y2="44"/><line x1="32" y1="50" x2="48" y2="50"/></g></svg>
  <div class="num">Service 4</div><div class="name">Access<br>Scaffolding</div><div class="more">Learn More</div>
</div>
<div class="abs" style="left:540px;top:1196px;width:120px;height:120px;background:var(--orange)"></div>
<div class="btn btn-dark" style="left:525px;top:1358px;width:150px">View All</div>
<div class="card" style="left:757px;top:1210px">
  <svg class="icon" viewBox="0 0 80 80"><rect x="16" y="16" width="48" height="48" transform="rotate(45 40 40)" fill="var(--orange)"/><g stroke="#fff" stroke-width="2" fill="none"><polyline points="26,40 40,26 54,40"/><rect x="30" y="40" width="20" height="16"/><line x1="40" y1="40" x2="40" y2="56"/><line x1="30" y1="48" x2="50" y2="48"/></g></svg>
  <div class="num">Service 5</div><div class="name">Temporary<br>Roofs</div><div class="more">Learn More</div>
</div>

<!-- WHY US -->
<div class="abs" style="left:0;top:1485px;width:1200px;height:701px;border-top:14px solid var(--orange);border-bottom:14px solid var(--orange);background:linear-gradient(180deg,#1f5b9a 0%,#2a6eae 35%,#6f6a5c 62%,#c88a3c 80%,#181410 100%)" role="img" aria-label="Scaffolding frame on a construction site against a blue sky at sunset"></div>
<div class="ghost" style="left:0;width:1200px;text-align:center;top:1572px;font-size:70px;color:rgba(0,0,0,.22)">WHY US</div>
<h2 class="heading" style="left:0;width:1200px;text-align:center;top:1598px;color:#fff">Why Us</h2>
<div class="stat" style="left:174px;top:1693px"><b>124</b><span>Total Years<br>of Experience</span></div>
<div class="stat" style="left:393px;top:1693px"><b>75</b><span>Projects<br>Completed</span></div>
<div class="stat" style="left:612px;top:1693px"><b>63</b><span>Clients<br>Satisfied</span></div>
<div class="stat" style="left:832px;top:1693px"><b>109</b><span>Ongoing<br>Projects</span></div>
<p class="abs why-text">Lorem ipsum dolor sit amet, consectetur adipiscing elit. Integer porta massa eu nunc tincidunt cursus. Maecenas consequat commodo viverra. Nunc aliquam non augue non dolor sit amet aliquet.</p>
<div class="abs cta">
  <p>CALL US ON 555-010-7890 OR CONTACT US NOW</p>
  <div class="btn btn-dark" style="left:632px;top:60px;width:152px">Contact Us</div>
</div>

<!-- ABOUT -->
<div class="abs" style="left:160px;top:2300px;width:468px;height:460px;clip-path:polygon(50% 0,100% 50%,50% 100%,0 50%);background:linear-gradient(180deg,#2e6fb0 0%,#6a9ac4 35%,#c28a47 65%,#7a4f28 100%)" role="img" aria-label="Tower crane and scaffolded building under construction"></div>
<div class="abs" style="left:178px;top:2530px;width:432px;height:230px;clip-path:polygon(0 0,100% 0,50% 100%);background:rgba(240,130,30,.0)"></div>
<div class="ghost" style="left:690px;top:2290px;font-size:72px">ABOUT</div>
<h2 class="heading" style="left:630px;top:2316px">About Us</h2>
<div class="abs about-box">
  <p>Lorem ipsum dolor sit amet, consectetur adipiscing elit, sed do eiusmod tempor incididunt ut labore et dolore magna aliqua. Sed libero enim sed faucibus turpis. Pretium viverra suspendisse potenti nullam. Egestas sed tempus urna et pharetra. Imperdiet sed euismod nisi porta lorem mollis aliquam ut porttitor.</p>
  <p>Netus et malesuada fames ac turpis. Sapien pellentesque habitant morbi tristique senectus et netus et. Orci nulla pellentesque dignissim enim sit amet venenatis. Mattis vulputate enim nulla aliquet. Scelerisque varius morbi enim nunc faucibus.</p>
</div>
<div class="btn btn-orange" style="left:626px;top:2693px;width:166px;box-shadow:0 4px 10px rgba(0,0,0,.15)">More About Us</div>

<!-- QUOTE -->
<section class="abs quote">
  <h2 class="heading" style="left:0;width:876px;text-align:center;top:30px;font-size:24px;color:#fff">Get a Quote</h2>
  <div class="field" style="left:56px;top:77px;width:239px;height:44px;line-height:44px">Your Name</div>
  <div class="field" style="left:319px;top:77px;width:238px;height:44px;line-height:44px">Your Email</div>
  <div class="field" style="left:581px;top:77px;width:239px;height:44px;line-height:44px">Telephone number</div>
  <div class="field" style="left:56px;top:146px;width:764px;height:109px;padding-top:18px">About your Project</div>
  <div class="upload">
    <svg style="margin-top:20px" width="24" height="24" viewBox="0 0 24 24"><g stroke="#fff" stroke-width="2" fill="none"><polyline points="7,8 12,3 17,8"/><line x1="12" y1="3" x2="12" y2="16"/><polyline points="3,15 3,21 21,21 21,15"/></g></svg>
    <div style="margin-top:8px">Choose a file or drag it here</div>
  </div>
</section>
<div class="btn btn-orange" style="left:517px;top:3224px;width:166px">Submit</div>

<!-- PORTFOLIO -->
<section class="abs portfolio" role="img" aria-label="Blue background with faint architectural blueprint lines"></section>
<div class="ghost" style="left:0;width:1200px;text-align:center;top:3462px;font-size:76px;color:rgba(0,0,0,.16)">PORTFOLIO</div>
<h2 class="heading" style="left:0;width:1200px;text-align:center;top:3488px;color:#fff">Portfolio</h2>
<div class="shot shot-a" style="left:0;width:125px" role="img" aria-label="Scaffolded building with red crane"></div>
<div class="shot shot-a" style="left:174px;width:254px" role="img" aria-label="Multi-storey building wrapped in scaffolding"></div>
<div class="abs feature" role="img" aria-label="Featured project photo with dark overlay">
  <div class="frame">
    <div style="margin-top:84px;font-size:12px;letter-spacing:2px;font-weight:600">PROJECT NAME</div>
    <div style="margin-top:22px;font-family:'Open Sans',sans-serif;font-size:10px;line-height:16px;color:#ccc">Medical Office<br>New Construction, State</div>
    <div style="margin-top:20px;font-size:10px;letter-spacing:2px;color:var(--orange);font-weight:600">VIEW PROJECT</div>
  </div>
</div>
<div class="shot shot-b" style="left:774px;width:254px" role="img" aria-label="Green tower crane above a building site"></div>
<div class="shot shot-a" style="left:1073px;width:127px" role="img" aria-label="Building under construction"></div>
<div class="arrow-btn" style="left:0">&#8249;</div>
<div class="arrow-btn" style="left:1152px">&#8250;</div>
<div class="btn btn-dark" style="left:533px;top:3941px;width:134px">View All</div>

<!-- NEWS -->
<div class="ghost" style="left:170px;top:4190px;font-size:68px">LATEST NEWS</div>
<h2 class="heading" style="left:174px;top:4196px">Latest News</h2>
<div class="btn btn-orange" style="left:893px;top:4195px;width:135px">Read All</div>

<article class="news" style="left:174px">
  <div class="img" style="background:linear-gradient(135deg,#f59a1c,#f4c02a 45%,#4a5e7a)" role="img" aria-label="Worker holding a yellow hard hat"></div>
  <div class="body"><div class="date">FEB 25 2020</div><h3>NEWS TITLE GOES HERE</h3><p>Lorem ipsum dolor sit amet, consectetur adipiscing elit. Integer porta massa eu nunc tin cidunt cursus. Maecenas consequat com...</p><div class="more">KEEP READING</div></div>
</article>
<article class="news" style="left:465px">
  <div class="img" style="background:linear-gradient(135deg,#6b4a30,#a37a52 50%,#c2452c)" role="img" aria-label="Construction tools laid out on a wooden surface"></div>
  <div class="body"><div class="date">FEB 25 2020</div><h3>NEWS TITLE GOES HERE</h3><p>Lorem ipsum dolor sit amet, consectetur adipiscing elit. Integer porta massa eu nunc tin cidunt cursus. Maecenas consequat com...</p><div class="more">KEEP READING</div></div>
</article>
<article class="news" style="left:757px">
  <div class="img" style="background:linear-gradient(135deg,#c9b9a3,#e07a28 50%,#5d6670)" role="img" aria-label="Site engineer in a safety vest reviewing a tablet"></div>
  <div class="body"><div class="date">FEB 25 2020</div><h3>NEWS TITLE GOES HERE</h3><p>Lorem ipsum dolor sit amet, consectetur adipiscing elit. Integer porta massa eu nunc tin cidunt cursus. Maecenas consequat com...</p><div class="more">KEEP READING</div></div>
</article>

<!-- FOOTER -->
<footer class="abs footer">
  <div class="brand" style="position:absolute;left:174px;top:110px;font-size:12px"><i></i>Corvithane</div>
  <ul class="fcol" style="left:174px;top:170px"><li>About Us</li><li>Portfolio</li><li>News</li><li>Contact Us</li></ul>
  <div class="fcol" style="left:378px"><h4>SERVICES</h4><ul><li>Commercial Scaffolding</li><li>Domestic Scaffolding</li><li>Industrial Scaffolding</li><li>Access Scaffolding</li><li>Temporary Roofs</li></ul></div>
  <div class="fcol" style="left:627px"><h4>LEGAL LINKS</h4><ul><li>Privacy Policy</li><li>Terms &amp; Conditions</li><li class="hl">Certifications</li><li>Resources</li></ul></div>
  <div class="fcol" style="left:853px"><h4>CONTACT INFO</h4><ul><li><i></i>555-010-3958</li><li><i></i>info@corvithane.com</li><li style="line-height:18px"><i></i>Address Line 1<br>&nbsp;&nbsp;&nbsp;&nbsp;Address Line 2<br>&nbsp;&nbsp;&nbsp;&nbsp;City, State 12345</li></ul></div>
  <div class="abs" style="left:174px;top:414px;width:854px;height:1px;background:#333"></div>
  <div class="copy">© 2020 Corvithane. All Rights Reserved.</div>
  <span class="social" style="left:880px" aria-label="Social link"></span>
  <span class="social" style="left:916px" aria-label="Social link"></span>
  <span class="social" style="left:952px;background:var(--orange)" aria-label="Social link"></span>
  <span class="social" style="left:988px" aria-label="Social link"></span>
  <span class="social" style="left:1024px" aria-label="Social link"></span>
</footer>

</body>
</html>
```